Web design for boutique law firm

Web design for law firm; practice areas include:
-international intellectual property counseling
-general corporate (contract negotiation, licensing, distribution agreements
-see my *very* outdated website at www.tbkcounsel.com: here is some of the home page content:

"TBK Law Group enjoys providing proactive, business-minded, efficient legal solutions for individuals and companies that benefit from major law firm experience at reasonable rates.

Some areas of emphasis include:

Counseling individuals and companies with respect to clearing, selecting, securing, managing, commercializing, and protecting intellectual property assets around the world. This includes traditional global brand management, marketing, advertising, and enforcement work as well as litigation.
TBK Law Group also provides general counseling services for individuals and businesses, from start-up advice to sophisticated business transactions strategy, agreement negotiating, dispute resolution, and litigation.
Before founding TBK Law Group in 2008, Curtis P. Langford led the Trademark, Copyright, & Brand Management Group for Halbrook & Pemberly's Seattle office. Curtis was also a senior associate at Silicon Valley based Thackery, Olmsted, Vance, & Bellweather."

Target Market(s)

Clients/potential clients needing tier one, international intellectual property advice with "mega" law firm experience for much less than what we were/would be charging at the "mega firms".

Industry/Entity Type

Legal

Number of Pages Required

4 page

Font styles to use
Serif
Sans Serif

Colors

Designer to choose colors to be used in the design.

Requirements
Must have
• +Improvement over everything on current site at www.tbkcounsel.com.
• +Pictures/bios for me and my team (four of us right now).
• +Easy to update and add/remove content.
• +Must be superior in design (look, feel, ease of use, classy and elegant, but hip, reflects international practice).
• +i have logos and color schemes (see current website) but will consider improvements.
Nice to have
• Let me know your thoughts.
Should not have
• No cheese; no overt sales pitches or marketing (since law firm).

```html
<!DOCTYPE html>
<html lang="en">
<head>
<meta charset="utf-8">
<title>TBK Law Group PLLC</title>
<link href="https://fonts.googleapis.com/css2?family=Montserrat:wght@400;500;600;700&family=Open+Sans:ital,wght@0,400;0,600;1,400&display=swap" rel="stylesheet">
<style>
:root{
  --orange:#f07125;
  --ink:#1d1d1d;
  --muted:#6d6d6d;
  --line:#d6d6d6;
  --dark:#353535;
  --white:#ffffff;
  --paper:#f2f2f2;
}
*{margin:0;padding:0;box-sizing:border-box}
html,body{width:1200px;height:2601px;overflow:hidden}
body{position:relative;background:var(--white);font-family:"Open Sans",Arial,sans-serif;color:var(--ink)}
.abs{position:absolute}

/* header */
.site-header{position:absolute;left:0;top:0;width:1200px;height:114px;background:var(--white)}
.brand{position:absolute;left:107px;top:50px;font-family:"Montserrat",Arial,sans-serif;font-weight:500;font-size:25px;color:var(--orange);letter-spacing:.5px}
.main-nav{position:absolute;top:60px;left:709px;font-family:"Montserrat",Arial,sans-serif;font-weight:600;font-size:14px}
.main-nav a{position:absolute;white-space:nowrap;color:var(--ink);text-decoration:none}
.main-nav a.active{color:var(--orange)}
.search-icon{position:absolute;left:1068px;top:61px}

/* hero */
.hero{position:absolute;left:0;top:114px;width:1200px;height:586px}
.hero-photo{position:absolute;inset:0;background:linear-gradient(100deg,#3b4249 0%,#5d6670 38%,#8c949b 62%,#3a3f47 100%)}
.hero-shade{position:absolute;inset:0;background:linear-gradient(90deg,rgba(20,22,26,.55),rgba(20,22,26,.1) 70%)}
.hero-title{position:absolute;left:139px;top:194px;font-family:"Montserrat",Arial,sans-serif;font-weight:600;font-size:41px;color:var(--orange);padding-bottom:4px;border-bottom:2px solid var(--orange)}
.hero-tagline{position:absolute;left:139px;top:250px;font-family:"Montserrat",Arial,sans-serif;font-weight:700;font-size:33px;color:var(--white);letter-spacing:1px;word-spacing:4px}
.hero-text{position:absolute;left:139px;top:297px;width:465px;font-size:13px;line-height:19px;color:#e9e9e9}
.btn-ghost{position:absolute;left:139px;top:380px;width:135px;height:42px;border:1.5px solid var(--white);border-radius:21px;color:var(--white);font-family:"Montserrat",Arial,sans-serif;font-weight:700;font-size:13px;line-height:39px;text-align:center}
.hero-arrows{position:absolute;left:1018px;top:455px}

/* practice areas */
.practice-card{position:absolute;top:642px;width:453px}
.practice-photo{width:453px;height:274px;box-shadow:0 3px 8px rgba(0,0,0,.25)}
.practice-title{margin-top:34px;font-family:"Montserrat",Arial,sans-serif;font-weight:700;font-size:22px;line-height:27px;letter-spacing:.6px;color:var(--ink)}
.practice-sub{margin-top:2px;font-size:11.5px;color:var(--ink)}

/* lawyers */
.lawyers{position:absolute;left:0;top:1044px;width:1200px;height:553px;background:var(--orange)}
.section-label{position:absolute;left:0;width:1200px;top:54px;text-align:center;font-family:"Montserrat",Arial,sans-serif;font-weight:700;font-size:20px;color:var(--white);letter-spacing:.5px}
.label-rule{position:absolute;left:569px;top:99px;width:73px;height:2px;background:var(--white)}
.lawyer-card{position:absolute;top:149px;width:234px;height:300px;background:var(--white);text-align:center}
.lawyer-photo{width:234px;height:226px}
.lawyer-name{margin-top:10px;font-family:"Montserrat",Arial,sans-serif;font-weight:700;font-size:20px;color:var(--ink);letter-spacing:.5px}
.lawyer-role{font-size:10px;font-style:italic;color:var(--ink)}
.lawyer-arrows{position:absolute;left:573px;top:482px}

/* contact */
.contact-title{position:absolute;left:0;width:1200px;top:1634px;text-align:center;font-family:"Montserrat",Arial,sans-serif;font-weight:400;font-size:32px;color:var(--orange)}
.contact-sub{position:absolute;left:0;width:1200px;top:1690px;text-align:center;font-family:"Montserrat",Arial,sans-serif;font-size:16px;color:var(--muted);letter-spacing:.5px}
.col-heading{position:absolute;font-family:"Montserrat",Arial,sans-serif;font-weight:500;font-size:20px;color:var(--orange)}
.detail{position:absolute;font-size:13px;color:#444;white-space:nowrap}
.map{position:absolute;left:147px;top:1904px;width:456px;height:205px;background:linear-gradient(120deg,#b9d4ec 0%,#d9e3d4 40%,#eae6d8 65%,#a9cbea 100%);border:1px solid var(--line)}
.field{position:absolute;left:648px;width:406px;height:42px;border:1px solid var(--line);background:var(--white);font-size:12px;color:#777;padding:12px 18px}
.btn-submit{position:absolute;left:648px;top:2075px;width:113px;height:34px;background:var(--orange);color:var(--white);font-size:13px;line-height:34px;text-align:center}

/* callout band */
.callout{position:absolute;left:0;top:2155px;width:1200px;height:169px;background:var(--dark)}
.callout-title{position:absolute;left:144px;top:49px;font-family:"Montserrat",Arial,sans-serif;font-size:26px;color:var(--white)}
.callout-text{position:absolute;left:144px;top:91px;font-size:13.5px;color:#e6e6e6}
.social{position:absolute;top:2225px;width:28px;height:28px;border-radius:50%;background:#8a8a8a}

/* footer */
.foot-heading{position:absolute;top:2348px;font-family:"Montserrat",Arial,sans-serif;font-weight:700;font-size:16px;color:var(--orange)}
.foot-links{position:absolute;left:146px;top:2386px;font-size:12.5px;line-height:22.5px;color:#333;list-style:none}
.news-input{position:absolute;left:329px;top:2390px;width:188px;height:34px;border:1px solid var(--line);font-size:12px;color:#444;padding:8px 12px}
.btn-subscribe{position:absolute;left:329px;top:2429px;width:115px;height:35px;background:var(--orange);color:var(--white);font-size:14px;line-height:35px;text-align:center}
.news-date{position:absolute;left:562px;width:38px;height:57px;background:var(--dark);color:var(--white);text-align:center;font-family:"Montserrat",Arial,sans-serif}
.news-date b{display:block;font-weight:400;font-size:18px;margin-top:8px;line-height:20px}
.news-date span{display:block;font-size:11px}
.news-text{position:absolute;left:617px;width:200px;font-size:12px;line-height:21px;color:#333}
.foot-brand{position:absolute;left:876px;top:2348px;font-family:"Montserrat",Arial,sans-serif;font-weight:500;font-size:17px;color:var(--orange);padding-bottom:2px;border-bottom:1px solid #999}
.foot-about{position:absolute;left:877px;top:2412px;width:222px;font-size:12px;line-height:19.5px;color:#333;text-align:justify}
.copyright{position:absolute;left:0;top:2568px;width:1200px;height:33px;background:var(--paper);text-align:center;font-size:11.5px;line-height:33px;color:#333}
</style>
</head>
<body>

<header class="site-header">
  <div class="brand">TBK LAW GROUP PLLC</div>
  <nav class="main-nav">
    <a class="active" style="left:0">Home</a>
    <a style="left:78px">Experience</a>
    <a style="left:194px">About</a>
    <a style="left:274px">Contact</a>
  </nav>
  <svg class="search-icon" width="14" height="14" viewBox="0 0 14 14" aria-hidden="true"><circle cx="5.5" cy="5.5" r="4" fill="none" stroke="#1d1d1d" stroke-width="2"/><line x1="8.5" y1="8.5" x2="13" y2="13" stroke="#1d1d1d" stroke-width="2"/></svg>
</header>

<section class="hero">
  <div class="hero-photo" role="img" aria-label="Photo of two smiling lawyers in suits working at a laptop in a bright office"></div>
  <div class="hero-shade"></div>
  <h1 class="hero-title">TBK Law Group PLLC</h1>
  <p class="hero-tagline">Imagine - Secure - Protect</p>
  <p class="hero-text">TBK Law Group enjoys providing proactive, business-minded, efficient legal solutions for individuals and companies that benefit from major law firm experience at reasonable rates</p>
  <div class="btn-ghost">LEARN MORE</div>
  <svg class="hero-arrows" width="56" height="24" viewBox="0 0 56 24" aria-hidden="true"><polyline points="14,4 6,12 14,20" fill="none" stroke="#fff" stroke-width="2.5"/><polyline points="42,4 50,12 42,20" fill="none" stroke="#fff" stroke-width="2.5"/></svg>
</section>

<article class="practice-card" style="left:130px">
  <div class="practice-photo" role="img" aria-label="Photo of a hand signing papers beside a small model house" style="background:linear-gradient(160deg,#6b7077 0%,#c9ccce 45%,#e6ecec 100%)"></div>
  <h2 class="practice-title">INTERNATIONAL INTELLECTUAL<br>PROPERTY COUNSELING</h2>
</article>
<article class="practice-card" style="left:619px">
  <div class="practice-photo" role="img" aria-label="Photo of a bright open-plan office with a presenter at a whiteboard" style="background:linear-gradient(160deg,#dfe4e8 0%,#f3f4f5 45%,#b7bcc1 100%)"></div>
  <h2 class="practice-title">GENERAL CORPORATE</h2>
  <p class="practice-sub">( Contract negotiation, licensing, distribution agreements )</p>
</article>

<section class="lawyers">
  <h2 class="section-label">LAWYERS</h2>
  <div class="label-rule"></div>
  <div class="lawyer-card" style="left:104px"><div class="lawyer-photo" role="img" aria-label="Portrait photo of Ruby" style="background:linear-gradient(180deg,#c9c9c9,#8c8580)"></div><div class="lawyer-name">RUBY</div><div class="lawyer-role">Lorium ipsum</div></div>
  <div class="lawyer-card" style="left:361px"><div class="lawyer-photo" role="img" aria-label="Portrait photo of Jhon" style="background:linear-gradient(180deg,#bdbdbd,#4a4a4c)"></div><div class="lawyer-name">JHON</div><div class="lawyer-role">Lorium ipsum</div></div>
  <div class="lawyer-card" style="left:616px"><div class="lawyer-photo" role="img" aria-label="Portrait photo of Jenny" style="background:linear-gradient(180deg,#b4b4b6,#b8524c)"></div><div class="lawyer-name">JENNY</div><div class="lawyer-role">Lorium ipsum</div></div>
  <div class="lawyer-card" style="left:872px"><div class="lawyer-photo" role="img" aria-label="Portrait photo of Roan" style="background:linear-gradient(180deg,#d6d6d6,#eeeeee)"></div><div class="lawyer-name">ROAN</div><div class="lawyer-role">Lorium ipsum</div></div>
  <svg class="lawyer-arrows" width="54" height="24" viewBox="0 0 54 24" aria-hidden="true"><polyline points="14,4 6,12 14,20" fill="none" stroke="#fff" stroke-width="2.5"/><polyline points="40,4 48,12 40,20" fill="none" stroke="#fff" stroke-width="2.5"/></svg>
</section>

<h2 class="contact-title">Contact Us</h2>
<p class="contact-sub">READY TO GET STARTED? GET IN TOUCH TODAY!</p>

<h3 class="col-heading" style="left:147px;top:1758px">ADDRESS</h3>
<svg class="abs" style="left:147px;top:1806px" width="14" height="14" viewBox="0 0 14 14" aria-hidden="true"><path d="M3 1 L5.5 1 L6.5 4 L5 5.5 C6 7.5 7 8.5 8.5 9 L10 7.5 L13 8.5 L13 11 C12.5 12.5 11 13 9.5 12.5 C5 11 2.5 8 1.5 4.5 C1 3 1.5 1.5 3 1 Z" fill="#444"/></svg>
<div class="detail" style="left:173px;top:1805px">206.555.0148</div>
<svg class="abs" style="left:146px;top:1838px" width="14" height="11" viewBox="0 0 14 11" aria-hidden="true"><rect x="0.75" y="0.75" width="12.5" height="9.5" fill="none" stroke="#444" stroke-width="1.5"/><polyline points="1,1 7,6 13,1" fill="none" stroke="#444" stroke-width="1.5"/></svg>
<div class="detail" style="left:173px;top:1835px">contact@tbkcounsel.com</div>
<svg class="abs" style="left:353px;top:1804px" width="12" height="17" viewBox="0 0 12 17" aria-hidden="true"><path d="M6 0 C2.7 0 0 2.7 0 6 C0 10 6 17 6 17 C6 17 12 10 12 6 C12 2.7 9.3 0 6 0 Z" fill="#333"/><circle cx="6" cy="6" r="2.2" fill="#fff"/></svg>
<div class="detail" style="left:381px;top:1805px">TBK LAW GROUP PLLC</div>
<div class="detail" style="left:381px;top:1835px">2250 Alder Street, Suite 410</div>
<div class="detail" style="left:381px;top:1865px">Seattle, WA 98121</div>
<div class="map" role="img" aria-label="Street map showing the office location"></div>

<h3 class="col-heading" style="left:650px;top:1751px">QUICK REQUEST</h3>
<div class="field" style="top:1803px">Name</div>
<div class="field" style="top:1862px">Email</div>
<div class="field" style="top:1921px">Phone Number</div>
<div class="field" style="top:1978px;height:86px">Message</div>
<div class="btn-submit">Submit</div>

<section class="callout">
  <h2 class="callout-title">Lorem ipsum dolor sit amet,</h2>
  <p class="callout-text">Sed ut perspiciatis unde omnis iste natus error sit voluptatem accusantium doloremque laudantium,</p>
</section>
<div class="social" style="left:921px"></div>
<div class="social" style="left:955px"></div>
<div class="social" style="left:988px"></div>
<div class="social" style="left:1023px"></div>

<h3 class="foot-heading" style="left:140px">Quick Links</h3>
<ul class="foot-links"><li>Home</li><li>Experience</li><li>About</li><li>Contact</li></ul>

<h3 class="foot-heading" style="left:329px">Newsletter</h3>
<div class="news-input">Enter Email id</div>
<div class="btn-subscribe">Subscribe</div>

<h3 class="foot-heading" style="left:558px">Latest News</h3>
<div class="news-date" style="top:2388px"><b>01</b><span>JAN</span></div>
<p class="news-text" style="top:2382px">Nemo enim ipsam voluptatem quia voluptas sit aspernatur aut odit aut fugit, sed quia</p>
<div class="news-date" style="top:2469px"><b>01</b><span>JAN</span></div>
<p class="news-text" style="top:2463px">Nemo enim ipsam voluptatem quia voluptas sit aspernatur aut odit aut fugit, sed quia</p>

<div class="foot-brand">TBK LAW GROUP PLLC</div>
<h3 class="foot-heading" style="left:875px;top:2380px">About Us</h3>
<p class="foot-about">Nam libero tempore, cum soluta nobis est eligendi optio cumque nihil impedit quo minus id quod maxime placeat facere possimus, omnis voluptas assumenda est,</p>

<footer class="copyright">Copyrights © 2017, www.companyname.com. All Rights Reserved.</footer>

</body>
</html>
```